Harborview Sight Fellowship Hall needs an ad/flyer for convention program

Established in 1949, the Harborview Sight Fellowship Hall's mission is to enrich the lives of blind and visually impaired adults by preparing them for a normal, active life in a society that is principally sighted by encouraging independence.

Located in Quillmont Green in San Diego, California, we are a nonprofit that gives blind and visually impaired people in our community an opportunity to socialize and interact. We help members build skills, confidence, and self-esteem through our various social, recreational, and educational activities. We were founded partially by Otter Society members and receive ongoing funding from them.

We need an 8 1/2 by 11 inch color ad in jpg format. We would like it to be editable. This will be the foundation of our rebranding. The ad will be in a meeting program of the California Otters (californiaotters-example.org) with the goal of highlighting some of our programs in order to solicit donations from individual Otter Societies, preferably ongoing ones.

We would like the ad to be generic enough that we can use the ad for other events and as a flyer in the future. We want the ad/flyer to be classic but eye popping with color. We want the design to reflect a professional and lively organization that loves to serve our members. We don’t entirely love our logo, but it’s what we have for now. Our next task will be a new logo design.

We would like to highlight some of our programs for our members include bingo, blind waterskiing and surfing, cooking and ceramic classes, foreign language classes, self defense classes, yoga, and craft classes. Many of the crafts our members make are sold during fundraisers, and they include blankets, scarves, beaded animals, and more. See a sampling of pictures. We provide transportation to and from our Center, free lunch while at the Center, and food to take home. Many of these activities continue during the pandemic via online platforms. We are doing monthly home deliveries of food to our members.

We need donations to keep our programs going, and we have building repairs & maintenance that we need donations in order to complete. See attached document regarding donations. Please reach out if you have questions. Thank you.

Web address: hvsfh-example.org
Street address: The Harborview Sight Fellowship Hall, 4472 Marrow Ln San Diego, CA 92188
Email address: donation@hvsfh-example.org
To make a donation: https://hvsfh-example.org/donate-2/

Target Market(s)

Donors

Industry/Entity Type

NonProfit

Font styles to use
Sans Serif

Requirements
Must have
• Highlight programs and information on how to make a donation.
Nice to have
• Information on how much each dollar donated will go - see attachment
Should not have
• Unprofessional or sloppy details

```html
<!DOCTYPE html>
<html lang="en">
<head>
<meta charset="utf-8">
<title>Harborview Sight Fellowship Hall – Donor Flyer</title>
<link href="https://fonts.googleapis.com/css2?family=Lato:wght@400;700;900&family=Oswald:wght@600;700&display=swap" rel="stylesheet">
<style>
  :root{
    --backdrop:#3f3f3f;
    --paper:#ffffff;
    --ink:#111111;
    --panel:#050505;
    --on-dark:#ffffff;
    --rule:#6a6a6a;
    --photo-light:#e9e6e2;
    --photo-mid:#b9b5b0;
    --photo-dark:#4a4644;
  }
  *{box-sizing:border-box;margin:0;padding:0}
  html,body{width:1200px;height:1200px;overflow:hidden;background:var(--backdrop)}
  .flyer{
    position:absolute;left:215px;top:115px;width:1234px;height:1587px;
    background:var(--paper);transform:scale(.6211);transform-origin:0 0;
    font-family:'Lato',sans-serif;color:var(--ink);overflow:hidden;
  }
  .org-name{
    position:absolute;left:80px;top:70px;width:420px;
    font-weight:900;font-size:40px;line-height:1.1;
  }
  .hero-photo{
    position:absolute;left:0;top:237px;width:1234px;height:487px;
    background:linear-gradient(100deg,var(--photo-light) 0%,var(--photo-mid) 45%,var(--photo-dark) 70%,var(--photo-mid) 100%);
  }
  .craft-circle{
    position:absolute;top:430px;width:266px;height:266px;border-radius:50%;
    background:var(--paper);padding:10px;
  }
  .craft-circle .ring{width:100%;height:100%;border-radius:50%;border:9px solid var(--ink);overflow:hidden}
  .craft-circle .fill{width:100%;height:100%}
  .angel{left:26px}
  .angel .fill{background:radial-gradient(circle at 50% 65%,#2350c9 0%,#5f7fd0 40%,#d9dbe0 75%)}
  .blankets{left:300px}
  .blankets .fill{background:linear-gradient(180deg,#3ba3d6 0%,#e9a9c9 30%,#f2e9ef 50%,#9a78c9 70%,#eab4cf 100%)}

  .pricing-title{position:absolute;left:52px;top:732px;font-family:'Oswald',sans-serif;font-weight:700;font-size:50px;line-height:1}
  .tier-pill{
    position:absolute;left:36px;top:787px;width:466px;height:40px;background:var(--ink);color:var(--on-dark);
    font-weight:900;font-size:22px;line-height:40px;padding-left:16px;border-radius:20px;
  }
  .tier-head{position:absolute;left:48px;font-family:'Oswald',sans-serif;font-weight:700;font-size:24px;line-height:30px}
  .tier-list{position:absolute;left:52px;width:580px;list-style:none}
  .tier-list li{font-size:23px;line-height:28px;padding-left:17px;text-indent:-17px;margin-bottom:8px}
  .tier-list li::before{content:"• "}
  .tier-list.ruled::after{content:"";display:block;width:460px;margin-left:8px;border-bottom:2px dotted var(--ink)}
  .tier-list.small li{font-size:21px;line-height:26px;width:470px}
  .grand{position:absolute;left:53px;top:1393px;font-family:'Oswald',sans-serif;font-weight:700;font-size:26px;line-height:29px}
  .note{position:absolute;left:53px;top:1455px;width:540px;font-size:21px;line-height:26px}

  .facts{
    position:absolute;left:682px;top:724px;width:552px;height:693px;
    background:var(--panel);color:var(--on-dark);border-bottom-left-radius:50px;
  }
  .facts h2{position:absolute;left:0;top:22px;width:100%;padding-left:10px;text-align:center;font-weight:900;font-size:33px;letter-spacing:.5px}
  .facts hr{position:absolute;left:40px;top:78px;width:440px;border:0;border-top:1px solid var(--rule)}
  .facts ol{list-style:none}
  .facts li{position:absolute;left:46px;width:436px;font-size:17px;line-height:21px;padding-left:19px;text-indent:-19px}

  .address{position:absolute;left:695px;top:1447px;width:500px;display:flex;gap:10px;font-size:19px;line-height:23px}
  .address svg{flex:none;margin-top:6px}

  .contact-bar{
    position:absolute;left:0;top:1519px;width:1234px;height:68px;background:var(--panel);color:var(--on-dark);
    display:flex;align-items:center;justify-content:space-between;padding:0 60px;font-size:21px;
  }
  .contact-bar span{display:flex;align-items:center;gap:12px}
</style>
</head>
<body>
<main class="flyer">
  <div class="org-name">Harborview Sight Fellowship Hall</div>

  <div class="hero-photo" role="img" aria-label="Photo of a beaded penguin in a Santa hat on a chunky knit blanket"></div>
  <div class="craft-circle angel"><div class="ring"><div class="fill" role="img" aria-label="Beaded blue angel ornament"></div></div></div>
  <div class="craft-circle blankets"><div class="ring"><div class="fill" role="img" aria-label="Stack of knitted blankets in pink, purple and blue"></div></div></div>

  <section class="pricing">
    <h2 class="pricing-title">PRE - COVID :</h2>
    <div class="tier-pill">$ 10 PER MONTH OR $120 WILL BUY :</div>
    <ul class="tier-list ruled" style="top:828px">
      <li><b>60 meals</b> for our lunch program – we serve <b>130 meals</b> each week</li>
      <li><b>13</b> round trip Bayline transportation tickets</li>
      <li>Enough beads to make <b>35</b> Marigold angels in our craft class</li>
    </ul>

    <div class="tier-head" style="top:998px">$20 PER MONTH OR $240 WILL BUY :</div>
    <ul class="tier-list ruled" style="top:1038px">
      <li><b>26</b> round trip Bayline transportation tickets</li>
      <li>One month of large print and Braille translation newsletter printing</li>
    </ul>

    <div class="tier-head" style="top:1143px">$50 PER MONTH OR $600 WILL BUY :</div>
    <ul class="tier-list ruled" style="top:1183px">
      <li><b>300 lunches</b></li>
      <li>Thanksgiving dinner with all the fixings for <b>80 to 100</b> guests</li>
    </ul>

    <div class="tier-head" style="top:1288px">$100 PER MONTH OR $1200 WILL BUY :</div>
    <ul class="tier-list small" style="top:1328px">
      <li>Approximately <b>10</b> Bingo parties including food and prizes.</li>
    </ul>

    <p class="grand">$1,083 PER MONTH OR $13,000 PER YEAR WILL<br>FUND OUR ENTIRE LUNCH PROGRAM FOR THE YEAR.</p>
    <p class="note">Every dollar donated goes to support HSF participants and programs.</p>
  </section>

  <aside class="facts">
    <h2>DID YOU KNOW ?</h2>
    <hr>
    <ol>
      <li style="top:104px">1. During the pandemic we offer Bingo, Trivia and other virtual games every week, where blind and low vision participants can win HSF bucks. You can sponsor one day of games for $35.</li>
      <li style="top:226px">2. You can provide 75 gift bags for our ‘We are in This Together’ home delivery program. Many of our blind and low vision people are isolated and stuck at home. These gift packages are welcomed with enthusiasm and gratefulness. Your rewards are huge smiles and happy faces.</li>
      <li style="top:383px">3. Our building is over 20 years old and requires ongoing maintenance and repairs</li>
      <li style="top:456px">4. Fencing (cage) required to protect outside air conditioning units from vandalism. Cost : $2,500</li>
      <li style="top:538px">5. Wanted: Sponsors for weekly virtual bingo and trivia games: Blind and Low vision participants receive one HSF buck per win. HSF bucks are turned into gift cards and Bayline transportation passes. Sponsor one week for $40. Sponsor 1 month for $160</li>
    </ol>
  </aside>

  <div class="address">
    <svg width="26" height="34" viewBox="0 0 26 34" aria-hidden="true"><path d="M13 0C5.8 0 0 5.6 0 12.6 0 22 13 34 13 34s13-12 13-21.4C26 5.6 20.2 0 13 0z" fill="#111"/><circle cx="13" cy="12.5" r="5" fill="#fff"/></svg>
    <span>The Harborview Sight Fellowship Hall, 4472 Marrow Ln San Diego, CA 92188</span>
  </div>

  <footer class="contact-bar">
    <span><svg width="22" height="16" viewBox="0 0 22 16" aria-hidden="true"><rect x="1" y="1" width="20" height="14" fill="#fff"/><path d="M1 1l10 8 10-8" stroke="#000" stroke-width="1.6" fill="none"/></svg>donation@hvsfh-example.org</span>
    <span><svg width="18" height="18" viewBox="0 0 18 18" aria-hidden="true"><g fill="none" stroke="#fff" stroke-width="1.4"><circle cx="9" cy="9" r="8"/><ellipse cx="9" cy="9" rx="3.5" ry="8"/><path d="M1 9h16M2.5 5h13M2.5 13h13"/></g></svg>hvsfh-example.org</span>
    <span><svg width="30" height="24" viewBox="0 0 30 24" aria-hidden="true"><g fill="none" stroke="#fff" stroke-width="1.5"><rect x="8" y="1" width="20" height="12" rx="1"/><circle cx="18" cy="7" r="3"/><path d="M1 16l6-3 8 2-5 1 9 0 6-3v3l-8 5H7l-6-2z"/></g></svg>https://hvsfh-example.org/donate-2/</span>
  </footer>
</main>
</body>
</html>
```